TrellanVita Website - Biologics storage and handling

I would like a beginning design on a website for TrellanVita:

A Boston-based company dedicated to sourcing, storing, and supplying biologic materials of all kinds to the life sciences and scientific markets. From starting reagents, to basic and intermediate materials, to final synthesized and engineered products, we provide value throughout the biologics supply chain. TrellanVita provides backup, overflow, emergency, and stocking storage solutions to companies on a temporary or permanent basis. Life sciences companies can take advantage of the fact that the company is located in the middle of the Boston/Cambridge biotechnology corridor in order to have quick and efficient access to their cold chain materials. Out of state companies can leverage TrellanVita’s location for efficient distribution of materials to partner and client organizations. We also provide other value added services to organizations that do not have the local manpower, such as sourcing, supply, and distribution of materials.

The design should be mostly a white background with clean, linear, geometric colors added in according to the blue and orange color scheme represented in the corporate logo attached.

The website needs to communicate reliable service and provide the concept of a company dedicated to handling and providing client biological samples in a secure and efficient manner.

Some local competitors are:
1. Korbel BioWorks: www.korbelbw.example
2. LabVault: www.labvault-store.example

From a design perspective, I like the Halvenor Thera website:

www.halvenorthera.example

Target Market(s)

Life sciences companies and other organizations

Industry/Entity Type

Biotechnology

Coding

Coded - Design and coding required

Number of Pages Required

5+ page

Font styles to use
Sans Serif

Colors
3176b5
0455a3
f37122

Requirements
Must have
• Tabs for pages:
About - Company information.
Platform - Inventory and sample management cloud platform; temperature profiling, logging, and reporting.
Services - Refrigeration and freezing services for biological samples, logistics services, sourcing services, courier services.
Updates - News, events, blog.
Login portal - Entry point for getting into platform. Maybe some freemium content here.
Nice to have
• Please be creative about website page sections, vibrant colors according to my established color scheme, and clean, linear, geometric shapes. I would like a white background with nice colors, clean lines and borders, and a very contemporary look. I want o
Should not have
• This is not a Business to Consumer business. This is a Business to Business enterprise. There should not be consumer oriented language. It is more about service and relationship management.

```html
<!DOCTYPE html>
<html lang="en">
<head>
<meta charset="utf-8">
<title>TrellanVita — Biologics Storage and Handling</title>
<link href="https://fonts.googleapis.com/css2?family=Poppins:wght@400;500;600&display=swap" rel="stylesheet">
<style>
:root{
  --teal:#1f5866;
  --teal-dark:#194b57;
  --orange:#e8670f;
  --ink:#1b1b1b;
  --muted:#777;
  --soft:#f5f5f5;
  --backdrop:#e8edef;
}
*{margin:0;padding:0;box-sizing:border-box}
html,body{width:712px;height:1200px;overflow:hidden;background:var(--backdrop);font-family:'Poppins',sans-serif;color:var(--ink)}
.page{position:absolute;left:145px;top:50px;width:421px;height:1098px;background:#fff;overflow:hidden;box-shadow:0 4px 18px rgba(0,0,0,.12)}
.abs{position:absolute}

/* top bar */
.topbar{left:0;top:0;width:421px;height:21px;background:var(--teal);color:#fff;font-size:3.8px;font-weight:500}
.topbar .item{position:absolute;top:0;height:21px;display:flex;align-items:center;gap:4px}
.topbar svg{width:9px;height:9px;stroke:#fff;fill:none;stroke-width:1.2}
.topbar .active-mark{position:absolute;left:127px;top:19px;width:17px;height:1.3px;background:var(--orange)}

/* nav */
.nav{left:0;top:21px;width:421px;height:26px;background:#fff}
.brand{position:absolute;display:flex;align-items:center;gap:3px;color:var(--teal);font-weight:500}
.brand .mark{width:8px;height:8px;background:var(--orange)}
.nav .brand{left:51px;top:8px;font-size:6.6px}
.menu{position:absolute;left:131px;top:11px;display:flex;gap:4px;font-size:3.4px;color:#aab3b6;white-space:nowrap}
.menu .current{color:var(--orange)}
.menu .sep{color:#ccc}
.login{position:absolute;left:346px;top:8px;width:26px;height:10.5px;background:var(--orange);color:#fff;font-size:3.3px;display:flex;align-items:center;justify-content:center}

/* hero */
.hero{left:0;top:47px;width:421px;height:172px;background:radial-gradient(ellipse at 50% 45%,#4d8799 0%,#34707f 55%,#245c6b 100%);color:#fff;text-align:center}
.hero h1{position:absolute;left:0;right:0;top:40px;font-size:16px;font-weight:600;line-height:16px}
.hero p{position:absolute;left:100px;right:100px;top:82px;font-size:5.2px;line-height:6.4px}
.hero .cta{position:absolute;left:181px;top:109px;width:58px;height:18px;background:var(--orange);font-size:5.8px;display:flex;align-items:center;justify-content:center;font-weight:500}
.dots{position:absolute;left:201px;top:161px;display:flex;gap:1.5px}
.dots i{display:block;width:3.2px;height:3.2px;background:#fff}
.dots i.on{background:var(--orange)}

/* about */
.about{left:0;top:219px;width:421px;height:177px;background:var(--soft)}
.h2{font-size:8.6px;font-weight:500;color:var(--ink)}
.about .h2{position:absolute;left:51px;top:45px}
.about p{position:absolute;left:51px;top:61px;width:157px;font-size:3.4px;line-height:6.1px;color:var(--muted)}
.btn{background:var(--orange);color:#fff;font-size:3.8px;font-weight:500;display:flex;align-items:center;justify-content:center}
.about .btn{position:absolute;left:51px;top:118px;width:37px;height:13px;border-radius:1px}
.about .photo{position:absolute;left:215px;top:29px;width:157px;height:120px;border-radius:4px;background:linear-gradient(135deg,#c23a55 0%,#e0406a 35%,#8e2c52 60%,#1f5a84 100%)}

/* services */
.services-title{left:0;width:421px;top:428px;text-align:center}
.service{position:absolute;width:100px;text-align:center}
.service .icon{width:31px;height:31px;margin:0 auto;border-radius:50%;border:1.2px solid var(--teal);display:flex;align-items:center;justify-content:center}
.service .icon span{width:26px;height:26px;border-radius:50%;background:var(--teal);display:flex;align-items:center;justify-content:center}
.service.hot .icon{border-color:var(--orange)}
.service.hot .icon span{background:var(--orange)}
.service .icon svg{width:14px;height:14px;stroke:#fff;fill:none;stroke-width:1.3;stroke-linecap:round}
.service h3{margin-top:11px;font-size:5.2px;font-weight:600;color:var(--teal)}
.service.hot h3{color:var(--orange)}
.service p{margin-top:2px;font-size:3.4px;line-height:4.6px;color:var(--muted)}
.service .more{margin-top:3px;font-size:3.8px;color:#e2432c;font-weight:500}

/* stories */
.stories-band{left:188px;top:644px;width:233px;height:141px;background:var(--teal)}
.quote-big{left:51px;top:680px;font-size:38px;line-height:38px;color:#e6e6e6;font-weight:600}
.stories-title{left:51px;top:716px;line-height:9.5px}
.arrows{left:51px;top:740px;display:flex;gap:6px}
.arrows svg{width:7px;height:6px;stroke:var(--ink);fill:none;stroke-width:1}
.story{position:absolute;top:681px;width:102px;height:67px;background:#fff;box-shadow:0 1px 6px rgba(0,0,0,.08);overflow:hidden}
.story .avatar{position:absolute;left:8px;top:20px;width:26px;height:26px;border-radius:50%;background:linear-gradient(160deg,#9aa5ad,#5a6670);border:0.8px solid var(--teal)}
.story .q{position:absolute;left:39px;top:6px;font-size:18px;line-height:18px;color:#ececec;font-weight:600}
.story p{position:absolute;left:39px;top:27px;width:58px;font-size:3.4px;line-height:4.8px;color:var(--muted)}
.story .name{position:absolute;left:39px;top:52px;font-size:4.5px;color:var(--orange)}

/* blogs */
.blogs-title{left:0;width:421px;top:816px;text-align:center}
.post{position:absolute;top:833px;width:102px;text-align:center}
.post .cover{height:67px}
.post h3{margin-top:13px;font-size:6.2px;line-height:6.7px;font-weight:500}
.post p{margin-top:3px;font-size:3.4px;line-height:5.2px;color:var(--muted)}
.post .btn{width:34px;height:12.5px;margin:8px auto 0;font-size:3.8px}

/* footer */
.footer{left:0;top:993px;width:421px;height:105px;background:var(--soft)}
.footer .brand{left:51px;top:32px;font-size:6.8px}
.footer .about-text{position:absolute;left:51px;top:51px;width:74px;font-size:3.4px;line-height:4.4px;color:var(--muted)}
.footer h4{position:absolute;top:31px;font-size:7px;font-weight:500;color:var(--orange)}
.links{position:absolute;top:43px;font-size:3.4px;line-height:7px;color:var(--muted)}
.contact{position:absolute;left:215px;top:43px;font-size:3.4px;color:var(--muted)}
.contact div{display:flex;gap:3px;align-items:flex-start;margin-bottom:3.2px;line-height:3.8px}
.contact svg{width:4px;height:4px;fill:var(--orange);flex:none}
.thumb{position:absolute;width:23px;height:17px}
.rule{position:absolute;left:51px;top:89px;width:321px;height:.6px;background:#ccc}
.copy{position:absolute;left:0;width:421px;top:95px;text-align:center;font-size:3.4px;color:var(--muted)}

.g-virus{background:linear-gradient(135deg,#0f3a4e,#1c6c84 60%,#0c2f40)}
.g-cells{background:radial-gradient(circle at 50% 55%,#c9b0e8 0%,#7fb6dd 30%,#2f7fb4 70%,#1c5f8c 100%)}
.g-dna{background:linear-gradient(135deg,#1a2228,#4f5e66 45%,#2a6d8e 60%,#11181d)}
</style>
</head>
<body>
<div class="page">

  <header class="abs topbar">
    <div class="item" style="left:86px">
      <svg viewBox="0 0 10 10"><path d="M2 1.5l2 .5.5 2-1 1a5 5 0 0 0 2.5 2.5l1-1 2 .5.5 2c-4 .5-8-3.5-7.5-7.5z"/></svg>(555) 014-2290
    </div>
    <div class="item" style="left:154px">
      <svg viewBox="0 0 10 10"><rect x="1" y="2" width="8" height="6"/><path d="M1 2l4 3.5L9 2"/></svg>INFO@TRELLANVITA.EXAMPLE
    </div>
    <div class="item" style="left:235px">
      <svg viewBox="0 0 10 10"><path d="M5 9S2 6 2 4a3 3 0 0 1 6 0c0 2-3 5-3 5z"/><circle cx="5" cy="4" r="1"/></svg>14 HARBOR LANE, CAMBRIDGE, MA 02139
    </div>
    <div class="active-mark"></div>
  </header>

  <nav class="abs nav">
    <div class="brand"><span class="mark"></span>TrellanVita</div>
    <div class="menu">
      <span class="current">HOME</span><span class="sep">|</span>
      <span>ABOUT US</span><span class="sep">|</span>
      <span>PLATFORM ⌄</span><span class="sep">|</span>
      <span>OUR SERVICES ⌄</span><span class="sep">|</span>
      <span>LATEST UPDATES ⌄</span><span class="sep">|</span>
      <span>CONTACT US</span>
    </div>
    <div class="login">LOG IN</div>
  </nav>

  <section class="abs hero" role="img" aria-label="Hero backdrop of blue DNA double helix strands">
    <h1>Biologics Storage<br>and Handling Services</h1>
    <p>Lorem Ipsum is simply dummy text of the printing and typesetting industry. Lorem Ipsum has been the industry's standard dummy text ever since the 1500s,</p>
    <div class="cta">CONTACT US</div>
    <div class="dots"><i></i><i class="on"></i><i></i><i></i></div>
  </section>

  <section class="abs about">
    <h2 class="h2">About Us</h2>
    <p>TrellanVita is dedicated to sourcing, storing, and supplying biologic materials of all kinds to the life sciences and scientific markets. From starting reagents, to basic and intermediate materials, to final synthesized and engineered products, we provide value throughout the biologics supply chain. TrellanVita provides backup, overflow, emergency, and stocking storage solutions to companies on a temporary or permanent basis. Life sciences companies can take advantage of the fact that the company is located in the middle of the Boston/Cambridge biotechnology corridor in order to have quick and efficient access to their cold chain materials.</p>
    <div class="btn">Read More</div>
    <div class="photo" role="img" aria-label="Photo of a pipette dropping red liquid into petri dishes"></div>
  </section>

  <h2 class="abs h2 services-title">Our Services</h2>

  <div class="service" style="left:52px;top:453px">
    <div class="icon"><span><svg viewBox="0 0 14 14"><path d="M7 1v12M1.8 4l10.4 6M1.8 10l10.4-6M5.5 2l1.5 1.5L8.5 2M5.5 12L7 10.5 8.5 12"/></svg></span></div>
    <h3>Refrigeration and Freezing</h3>
    <p>Lorem Ipsum is simply dummy text of the printing and typesetting industry. Lorem Ipsum has been the industry's standard dummy text ever.</p>
    <div class="more">Read More</div>
  </div>
  <div class="service hot" style="left:160px;top:453px">
    <div class="icon"><span><svg viewBox="0 0 14 14"><circle cx="7" cy="7" r="5"/><circle cx="5.5" cy="6" r="1"/><circle cx="8.5" cy="5.5" r=".6"/><path d="M5.5 9h3"/></svg></span></div>
    <h3>Biological Samples</h3>
    <p>Lorem Ipsum is simply dummy text of the printing and typesetting industry. Lorem Ipsum has been the industry's standard dummy text ever</p>
    <div class="more">Read More</div>
  </div>
  <div class="service" style="left:269px;top:453px">
    <div class="icon"><span><svg viewBox="0 0 14 14"><path d="M1 9.5h12M2 9.5V7h3V4.5h3l2 2.5h2v2.5"/><circle cx="4" cy="10.5" r="1"/><circle cx="10" cy="10.5" r="1"/></svg></span></div>
    <h3>Logistics Services</h3>
    <p>Lorem Ipsum is simply dummy text of the printing and typesetting industry. Lorem Ipsum has been the industry's standard dummy text ever</p>
    <div class="more">Read More</div>
  </div>
  <div class="service" style="left:106px;top:546px">
    <div class="icon"><span><svg viewBox="0 0 14 14"><circle cx="7" cy="6" r="2"/><path d="M7 8v4"/></svg></span></div>
    <h3>Sourcing Services</h3>
    <p>Lorem Ipsum is simply dummy text of the printing and typesetting industry. Lorem Ipsum has been the industry's standard dummy text ever.</p>
    <div class="more">Read More</div>
  </div>
  <div class="service" style="left:215px;top:546px">
    <div class="icon"><span><svg viewBox="0 0 14 14"><rect x="4" y="2" width="6" height="5"/><path d="M7 2v2M1.5 10h3l2 1.5h4l2-2"/></svg></span></div>
    <h3>Courier Services</h3>
    <p>Lorem Ipsum is simply dummy text of the printing and typesetting industry. Lorem Ipsum has been the industry's standard dummy text ever</p>
    <div class="more">Read More</div>
  </div>

  <div class="abs stories-band"></div>
  <div class="abs quote-big">“</div>
  <h2 class="abs h2 stories-title">Customer<br>Stories</h2>
  <div class="abs arrows">
    <svg viewBox="0 0 7 6"><path d="M6.5 3H.8M3 .8L.8 3 3 5.2"/></svg>
    <svg viewBox="0 0 7 6"><path d="M.5 3h5.7M4 .8L6.2 3 4 5.2"/></svg>
  </div>

  <div class="story" style="left:120px">
    <div class="avatar" role="img" aria-label="Client portrait"></div>
    <div class="q">“</div>
    <p>Lorem Ipsum is simply dummy text of the printing and typesetting industry. Lorem Ipsum has been the industry's</p>
    <div class="name">John Doe</div>
  </div>
  <div class="story" style="left:228px">
    <div class="avatar" role="img" aria-label="Client portrait"></div>
    <div class="q">“</div>
    <p>Lorem Ipsum is simply dummy text of the printing and typesetting industry. Lorem Ipsum has been the industry's</p>
    <div class="name">John Doe</div>
  </div>
  <div class="story" style="left:337px;width:84px">
    <div class="avatar" role="img" aria-label="Client portrait"></div>
    <div class="q">“</div>
    <p>Lorem Ipsum is simply dummy text of the printing and typesetting industry. Lorem Ipsum has been the industry's</p>
    <div class="name">John Doe</div>
  </div>

  <h2 class="abs h2 blogs-title">Our Blogs</h2>

  <article class="post" style="left:52px">
    <div class="cover g-virus" role="img" aria-label="Illustration of virus particles on dark blue"></div>
    <h3>Possit Nostro Aeterno Eu Vis, Ut Cum Quem Reque</h3>
    <p>Lorem Ipsum is simply dummy text of the printing and typesetting industry. Lorem Ipsum has been the industry's standard dummy text ever since the 1500s,</p>
    <div class="btn">Read More</div>
  </article>
  <article class="post" style="left:161px">
    <div class="cover g-cells" role="img" aria-label="Illustration of blue and violet cells"></div>
    <h3>Possit Nostro Aeterno Eu Vis, Ut Cum Quem Reque</h3>
    <p>Lorem Ipsum is simply dummy text of the printing and typesetting industry. Lorem Ipsum has been the industry's standard dummy text ever since the 1500s,</p>
    <div class="btn">Read More</div>
  </article>
  <article class="post" style="left:269px">
    <div class="cover g-dna" role="img" aria-label="Illustration of a DNA helix with a test tube"></div>
    <h3>Possit Nostro Aeterno Eu Vis, Ut Cum Quem Reque</h3>
    <p>Lorem Ipsum is simply dummy text of the printing and typesetting industry. Lorem Ipsum has been the industry's standard dummy text ever since the 1500s,</p>
    <div class="btn">Read More</div>
  </article>

  <footer class="abs footer">
    <div class="brand"><span class="mark"></span>TrellanVita</div>
    <p class="about-text">Lorem Ipsum is simply dummy text of the printing and typesetting industry. Lorem Ipsum has been the industry's standard dummy text ever since the 1500s,</p>

    <h4 style="left:133px">Menu</h4>
    <div class="links" style="left:133px">Home<br>About Us<br>Services<br>Gallery<br>Blogs</div>
    <div class="links" style="left:160px">Contact us<br>Terms &amp; condition<br>Privacy Policy<br>Events<br>Features</div>

    <h4 style="left:215px">Contact Us</h4>
    <div class="contact">
      <div><svg viewBox="0 0 4 4"><path d="M2 4S.5 2.5.5 1.6a1.5 1.5 0 0 1 3 0C3.5 2.5 2 4 2 4z"/></svg><span>Monday-Friday: 7am to 5pm<br>Dispatch: 24 / 7</span></div>
      <div><svg viewBox="0 0 4 4"><path d="M.6.4l1 .3.2.9-.4.4a2 2 0 0 0 .9.9l.4-.4.9.2.3 1C1.8 3.9.1 2.2.6.4z"/></svg><span>(+1) 555-014-7781</span></div>
      <div><svg viewBox="0 0 4 4"><rect x=".3" y=".8" width="3.4" height="2.4"/></svg><span>info@trellanvita.example</span></div>
      <div><svg viewBox="0 0 4 4"><circle cx="2" cy="2" r="1.7"/></svg><span>www.trellanvita.example</span></div>
    </div>

    <h4 style="left:296px">Gallery</h4>
    <div class="thumb g-virus" style="left:296px;top:41px" role="img" aria-label="Gallery image of virus particles"></div>
    <div class="thumb g-dna" style="left:322px;top:41px" role="img" aria-label="Gallery image of DNA helix"></div>
    <div class="thumb g-cells" style="left:349px;top:41px" role="img" aria-label="Gallery image of cells"></div>
    <div class="thumb g-cells" style="left:296px;top:61px" role="img" aria-label="Gallery image of cells"></div>
    <div class="thumb g-virus" style="left:322px;top:61px" role="img" aria-label="Gallery image of virus particles"></div>
    <div class="thumb g-dna" style="left:349px;top:61px" role="img" aria-label="Gallery image of DNA helix"></div>

    <div class="rule"></div>
    <div class="copy">Copyright ©2020 All rights reserved</div>
  </footer>
</div>
</body>
</html>
```